Food Safety 1-California workers only

3.25" by 4.5" Black and White Magazine Ad
This ad is to train California workers only.
Workers will be trained on: Food Safety, FSMA (Food Safety Modernization Act), using equipment safety, food processing production skills, worker safety, supervisory skills, communication skills.
"FREE TRAINING", The company does the training or Harbor Learning will provide the training.
Training grants range from $100,000 to $400,000.
Companies must be in business for profit.
Companies must train 200 employees or more.
This program is for California workers only.
Incumbent or new-hires are eligible.

Target Market(s)

California food processors, farms, food packaging, food processors, companies under FSMA, food safety, food production who need to train employees.

Industry/Entity Type

Food Production

Font styles to use
Serif
Sans Serif

Colors

Designer to choose colors to be used in the design.

Requirements
Must have
• This is a 3.25 inch by 4.5 inch magazine ad. It must be black and white. No color.
• The deliverable must be in basic PhotoShop. The ad does not need to include any graphics and be text only if needed. If you have a black and white graphic that will show well.
• Look at www.BQXFoodSafety..com
• Use the text from "FOOD2U-Photoshop-052018" file as your starting point.
Nice to have
• A black and white graphic about food. See www.BQXFoodSafety.com
Should not have
• No color.

```html
<!DOCTYPE html>
<html lang="en">
<head>
<meta charset="utf-8">
<title>Free Training – Harbor Learning Company</title>
<link rel="stylesheet" href="https://fonts.googleapis.com/css2?family=Antonio:wght@400;500;700&family=Open+Sans:wght@300;700&display=swap">
<style>
  :root {
    --ink: #000000;
    --paper: #ffffff;
    --backdrop: #e9eff6;
  }
  html, body {
    margin: 0;
    padding: 0;
    width: 1200px;
    height: 1200px;
    overflow: hidden;
    background: var(--backdrop);
  }
  .ad {
    position: absolute;
    left: 203px;
    top: 50px;
    width: 818px;
    height: 1134px;
    transform: scale(0.97);
    transform-origin: top left;
    background: var(--paper);
  }
  .ad svg { display: block; }
  .condensed { font-family: "Antonio", "Arial Narrow", sans-serif; }
  .humanist { font-family: "Open Sans", Arial, sans-serif; }
  .title { font-weight: 700; font-size: 170px; fill: var(--paper); }
  .topics { font-weight: 500; font-size: 40px; fill: var(--paper); }
  .slogan { font-size: 38px; fill: var(--ink); font-weight: 300; }
  .slogan .strong { font-weight: 700; }
  .or-label { font-weight: 700; font-size: 24px; fill: var(--paper); }
  .qualify-heading { font-weight: 700; font-size: 72px; fill: var(--ink); }
  .rule { stroke: var(--ink); stroke-width: 2; }
  .requirement { font-weight: 500; font-size: 29px; fill: var(--ink); }
  .tick { fill: none; stroke: var(--ink); stroke-width: 1.8; stroke-linecap: round; stroke-linejoin: round; }
  .contact-name { font-weight: 500; font-size: 34px; fill: var(--ink); }
  .contact-line { font-weight: 500; font-size: 27px; fill: var(--ink); }
  .phone { font-weight: 700; font-size: 48px; fill: var(--paper); }
  .band { fill: var(--ink); }
  .swoosh { fill: none; stroke: var(--paper); stroke-width: 3; }
</style>
</head>
<body>
<main class="ad">
  <svg width="818" height="1134" viewBox="0 0 818 1134" xmlns="http://www.w3.org/2000/svg">
    <!-- header band -->
    <g class="header" transform="translate(32,33)">
      <path class="band" d="M0,12 Q0,0 12,0 H743 Q755,0 755,12 V222 C520,212 240,222 0,250 Z"/>
      <path class="swoosh" d="M0,243 C230,216 520,204 755,212"/>
      <text class="condensed title" x="18" y="143" textLength="720" lengthAdjust="spacingAndGlyphs">FREE TRAINING</text>
      <text class="condensed topics" x="18" y="189" textLength="718" lengthAdjust="spacingAndGlyphs">FOOD SAFETY • FSMA • PRODUCTION SKILLS • WORKER SAFETY</text>
    </g>

    <!-- slogans -->
    <g class="slogans" text-anchor="middle">
      <text class="humanist slogan" x="410" y="342">“<tspan class="strong">YOU DO</tspan> THE TRAINING AND</text>
      <text class="humanist slogan" x="410" y="380">THE STATE OF <tspan class="strong">CALIFORNIA PAYS FOR IT!</tspan>”</text>
      <ellipse cx="409" cy="408" rx="36" ry="20" fill="var(--ink)"/>
      <text class="humanist or-label" x="409" y="417">OR</text>
      <text class="humanist slogan" x="410" y="468">“<tspan class="strong">WE DO</tspan> THE TRAINING AND</text>
      <text class="humanist slogan" x="410" y="506"><tspan class="strong">THE STATE PAYS FOR IT!</tspan>”</text>
    </g>

    <!-- qualification -->
    <g class="qualify">
      <line class="rule" x1="57" y1="548" x2="228" y2="548"/>
      <line class="rule" x1="57" y1="785" x2="228" y2="785"/>
      <text class="condensed qualify-heading" x="57" y="656" textLength="175" lengthAdjust="spacingAndGlyphs">HOW TO</text>
      <text class="condensed qualify-heading" x="57" y="723" textLength="175" lengthAdjust="spacingAndGlyphs">QUALIFY:</text>
    </g>

    <defs>
      <g id="tick-icon">
        <path class="tick" d="M20,7 A10,10 0 1 0 22,13"/>
        <path class="tick" d="M7,11 L11.5,15.5 L23,4"/>
      </g>
    </defs>
    <g class="requirements">
      <use href="#tick-icon" x="257" y="549"/>
      <text class="condensed requirement" x="296" y="571">Train California Workers Only</text>
      <use href="#tick-icon" x="257" y="584"/>
      <text class="condensed requirement" x="296" y="606">Trainees must earn $11/hour</text>
      <use href="#tick-icon" x="257" y="619"/>
      <text class="condensed requirement" x="296" y="641">Full-time workers only</text>
      <use href="#tick-icon" x="257" y="654"/>
      <text class="condensed requirement" x="296" y="676" textLength="477" lengthAdjust="spacingAndGlyphs">Employees must attend at least 8 Hours of training</text>
      <use href="#tick-icon" x="257" y="689"/>
      <text class="condensed requirement" x="296" y="711">You must train 200 or more employees</text>
      <use href="#tick-icon" x="257" y="724"/>
      <text class="condensed requirement" x="296" y="746">Incumbent or New-Hire workers are eligible</text>
      <use href="#tick-icon" x="257" y="759"/>
      <text class="condensed requirement" x="296" y="781">Seasonal workers are eligible</text>
    </g>

    <!-- contact -->
    <g class="contact" text-anchor="middle">
      <text class="condensed contact-name" x="410" y="851">Contact Daniel Corwin at Harbor Learning Company, Inc.</text>
      <text class="condensed contact-line" x="410" y="900">1200 Seabreeze Avenue, Suite 310, Irvine, CA 92618</text>
      <text class="condensed contact-line" x="410" y="940">www.HLCCAL.com | www.BQXFoodSafety.com</text>
      <text class="condensed contact-line" x="410" y="979">email: Dan.Corwin@HLCCAL.com</text>
    </g>

    <!-- footer band -->
    <g class="footer" transform="translate(32,976)">
      <path class="band" d="M0,2 C250,22 520,14 755,0 V115 Q755,127 743,127 H12 Q0,127 0,115 Z"/>
      <path class="swoosh" d="M0,12 C250,32 520,22 755,8"/>
      <text class="condensed phone" x="378" y="104" text-anchor="middle">Call (949) 555-0148</text>
    </g>
  </svg>
</main>
</body>
</html>
```